QUOTE Graphics for Summer Challenge

I would like to put these quotes over one of the pictures attached; For Instagram, use new size: 4:5 (1080 x 1350 pixels). One Quote per picture, and I want the quote to be bold or easy to read as well. I provided a few reference graphics that I really like as examples below.
All of the pictures are attached; you can pick any photo and add one quote to it; but no stock photography
All the quotes are in the attached WORD document

```html
<!DOCTYPE html>
<html lang="en">
<head>
<meta charset="utf-8">
<title>Sun Glow Summer Reset — Quote Graphics</title>
<link rel="stylesheet" href="https://fonts.googleapis.com/css2?family=Playfair+Display:wght@400&family=Oswald:wght@300&display=swap">
<style>
  :root {
    --canvas: #1a2438;
    --ink: #ffffff;
    --box-charcoal: rgba(44, 40, 44, 0.82);
    --box-navy: rgba(52, 62, 112, 0.78);
    --box-slate: rgba(66, 74, 110, 0.72);
    --box-deep: rgba(40, 70, 110, 0.78);
    --panel-gray: rgba(60, 60, 62, 0.9);
  }
  * { box-sizing: border-box; margin: 0; padding: 0; }
  html, body { width: 1200px; height: 610px; overflow: hidden; background: var(--canvas); }
  .grid { position: relative; width: 1200px; height: 610px; }
  .tile { position: absolute; width: 228px; height: 285px; overflow: hidden; }
  .photo { position: absolute; inset: 0; }
  .quote-box { position: absolute; color: var(--ink); padding: 6px 9px; }
  .headline { font-family: "Playfair Display", Georgia, serif; font-weight: 400; }
  .headline span, .cta span, .side-panel span { display: block; white-space: nowrap; }
  .cta { font-family: "Oswald", "Arial Narrow", sans-serif; font-weight: 300; margin-top: 3px; }
  .side-panel { position: absolute; left: 0; top: 0; width: 123px; height: 285px; background: var(--panel-gray); color: var(--ink); padding: 34px 0 0 15px; }
  .side-panel p { font-family: "Playfair Display", Georgia, serif; font-size: 14px; line-height: 23px; }
</style>
</head>
<body>
<main class="grid">

  <section class="tile" style="left:13px; top:16px;">
    <div class="photo" role="img" aria-label="Black and white portrait of a woman in a crochet swimsuit" style="background:linear-gradient(160deg,#d8d8d8,#7a7a7a 55%,#3c3c3c);"></div>
    <div class="quote-box" style="left:9px; top:126px; width:212px; height:130px; background:var(--box-charcoal); padding:4px 7px;">
      <h2 class="headline" style="font-size:25px; line-height:29px;"><span>Feeling bloated,</span><span>sluggish, and</span><span>too big?</span></h2>
      <p class="cta" style="font-size:11.5px; line-height:16px; text-align:center;"><span>Your detox starts now. Comment SUMMER to</span><span>join the Sun Glow Summer Reset</span></p>
    </div>
  </section>

  <section class="tile" style="left:250px; top:16px;">
    <div class="photo" role="img" aria-label="Woman in sunglasses posing at an infinity pool with hills behind" style="background:linear-gradient(180deg,#a08cc0 0%,#5f7a55 14%,#3a8fd0 28%,#4ea6e0 70%,#d9c3a8 100%);"></div>
    <div class="quote-box" style="left:21px; top:134px; width:185px; height:136px; background:var(--box-navy); padding:10px 9px;">
      <h2 class="headline" style="font-size:16.5px; line-height:18px;"><span>You don’t need</span><span>motivation.You need</span><span>a proven plan and</span><span>some accountability.</span></h2>
      <p class="cta" style="font-size:11.5px; line-height:14px; margin-top:6px;"><span>Comment SUN GLOW to get</span><span>join us July 7th</span></p>
    </div>
  </section>

  <section class="tile" style="left:487px; top:16px;">
    <div class="photo" role="img" aria-label="Black and white photo of a woman in a sheer dress by a pool" style="background:linear-gradient(170deg,#c9c9c9,#8d8d8d 50%,#555);"></div>
    <div class="quote-box" style="left:15px; top:123px; width:197px; height:136px; background:var(--box-charcoal); padding:8px 9px;">
      <h2 class="headline" style="font-size:15.5px; line-height:18.6px;"><span>Need a jumpstart?</span><span>We’re detoxing,</span><span>burning fat, and getting</span><span>snatched.</span></h2>
      <p class="cta" style="font-size:12px; line-height:17px; margin-top:4px;"><span>Comment SUN GLOW to join us on</span><span>July 7th</span></p>
    </div>
  </section>

  <section class="tile" style="left:724px; top:16px;">
    <div class="photo" role="img" aria-label="Blue-toned photo of a smiling woman in sunglasses by the water" style="background:linear-gradient(160deg,#c9d2e3,#7d8db3 50%,#2e3f78);"></div>
    <div class="quote-box" style="left:16px; top:131px; width:195px; height:137px; background:var(--box-slate); padding:12px 14px;">
      <h2 class="headline" style="font-size:16px; line-height:17.7px;"><span>This Sun Glow Summer</span><span>Reset plan is</span><span>helping women drop</span><span>pounds and feel</span><span>sexy again.</span></h2>
      <p class="cta" style="font-size:13px; line-height:17px; margin-top:2px;"><span>Comment SUMMER to join us</span></p>
    </div>
  </section>

  <section class="tile" style="left:960px; top:16px;">
    <div class="photo" role="img" aria-label="Sepia-toned photo of a woman in a crochet swimsuit outdoors" style="background:linear-gradient(160deg,#8f8682,#5f5552 50%,#3b3432);"></div>
    <div class="quote-box" style="left:17px; top:137px; width:192px; height:123px; background:var(--box-charcoal); padding:7px 9px;">
      <h2 class="headline" style="font-size:16px; line-height:17.7px;"><span>Summer’s here,</span><span>but your body doesn’t</span><span>feel ready?</span></h2>
      <p class="cta" style="font-size:12px; line-height:16px; margin-top:2px;"><span>You’re not too late. Comment</span><span>SUMMER to join the Sun Glow</span><span>Summer Reset</span></p>
    </div>
  </section>

  <section class="tile" style="left:13px; top:310px;">
    <div class="photo" role="img" aria-label="Woman in a long sheer dress standing in an infinity pool above green hills" style="background:linear-gradient(180deg,#5b7a4a 0%,#4d6a5a 22%,#2f6fc0 34%,#1e5fb8 70%,#3d7cd0 100%);"></div>
    <div class="quote-box" style="left:14px; top:121px; width:200px; height:134px; background:var(--box-deep); padding:5px 10px;">
      <h2 class="headline" style="font-size:17.5px; line-height:20.5px;"><span>Your belly bloat</span><span>and stubborn</span><span>weight gain aren’t</span><span>going anywhere…</span></h2>
      <p class="cta" style="font-size:12px; line-height:18px; margin-top:2px;"><span>unless you do something different.</span><span>Comment SUN GLOW to join us!</span></p>
    </div>
  </section>

  <section class="tile" style="left:250px; top:310px;">
    <div class="photo" role="img" aria-label="Black and white photo of a smiling woman in a sheer dress" style="background:linear-gradient(160deg,#e3e3e3,#a0a0a0 50%,#4a4a4a);"></div>
    <div class="side-panel">
      <p><span>If you feel like</span><span>you’ve let</span><span>yourself</span><span>go lately, this is</span><span>your jumpstart.</span><span>Comment</span><span>SUMMER to</span><span>join the Sun</span><span>Glow Summer</span><span>Reset</span></p>
    </div>
  </section>

  <section class="tile" style="left:487px; top:310px;">
    <div class="photo" role="img" aria-label="Warm-toned photo of a woman in a leopard swimsuit sitting on the sand" style="background:linear-gradient(170deg,#e6c2b6,#c49483 55%,#7a5448);"></div>
    <div class="quote-box" style="left:16.5px; top:131px; width:194px; height:126px; background:var(--box-charcoal); padding:8px 7px;">
      <h2 class="headline" style="font-size:18.5px; line-height:23px;"><span>Cravings, belly fat,</span><span>and water weight?</span></h2>
      <p class="cta" style="font-size:12.5px; line-height:18px; margin-top:3px;"><span>Say goodbye in 30 days. Comment</span><span>SUMMER to join the Sun Glow</span><span>Summer Reset</span></p>
    </div>
  </section>

  <section class="tile" style="left:724px; top:310px;">
    <div class="photo" role="img" aria-label="Soft green-toned photo of a woman in a leopard swimsuit smiling over her shoulder" style="background:linear-gradient(170deg,#b8c7bc,#8fa396 55%,#6a7368);"></div>
    <div class="quote-box" style="left:17.5px; top:147px; width:192px; height:116px; background:var(--box-charcoal); padding:6px 7px;">
      <h2 class="headline" style="font-size:19.5px; line-height:20.5px;"><span>We’re getting a tiny</span><span>waist and dropping</span><span>pounds together.</span></h2>
      <p class="cta" style="font-size:13px; line-height:17px; margin-top:5px;"><span>Don’t miss this. Comment</span><span>SUN GLOW to join</span></p>
    </div>
  </section>

  <section class="tile" style="left:960px; top:310px;">
    <div class="photo" role="img" aria-label="Woman in a swimsuit in an infinity pool overlooking a hillside town" style="background:linear-gradient(180deg,#4a8fb0 0%,#8aa59b 25%,#2f7fb5 50%,#2ea0d0 80%,#5fc2e0 100%);"></div>
    <div class="quote-box" style="left:8px; top:131px; width:210px; height:124px; background:var(--box-deep); padding:8px 8px;">
      <h2 class="headline" style="font-size:21.5px; line-height:25px;"><span>The scale keeps</span><span>climbing and</span><span>nothing’s working?</span></h2>
      <p class="cta" style="font-size:13px; line-height:18px; margin-top:1px;"><span>This challenge is your lifeline.</span><span>Comment SUN GLOW to join now!</span></p>
    </div>
  </section>

</main>
</body>
</html>
```